Flyer-Design für Ferienhaus auf Sylt
Zielgruppe
Ferienhaus auf Sylt im ruhigen und traditionellen Ort Archsum. Zielgruppe ruhe- und erholungssuchende Erwachsene, Familien mit Kind und evtl. mit Hund. Ferienhaus 'klein, aber fein' in ruhiger Lager mit großem Grundstück.
Homepage: duenenkate-wiesmoor.de
Aufgabenstellung
Format DIN LANG / 4 Seiten: Es sollen keine Saisonzeiten und auch keine Preise genannt werden. Es soll nur genannt werden, dass das Haus ab 50 EUR / Tag gemietet werden kann. Bitte nicht die vollständige Adresse des Objektes angeben, lediglich „Sylt-Archsum“. Kontakdtaen bitte auf der Rückseite nennen (siehe Homepage). Kontaktaufnahme bevorzugt per Mail / Anfrageformular v. Homepage. Gerne meine Bilder nutzen, bin aber auch offen für 2-3 Bilder aus dem Stock. Kleine Texte formulieren und gerne mehrere Bilder des Hauses zeigen.

```html
<!DOCTYPE html>
<html lang="de">
<head>
<meta charset="utf-8">
<title>Ferienhaus auf Sylt – Flyer Titelseite</title>
<link href="https://fonts.googleapis.com/css2?family=Sacramento&family=Montserrat:wght@400;700&family=Questrial&display=swap" rel="stylesheet">
<style>
  :root {
    --canvas: #d4d4d4;
    --sky-top: #93bddd;
    --sky-bottom: #b4d3ea;
    --band: #17b4dc;
    --band-deep: #11a6cf;
    --paper: #ffffff;
    --lawn: #5e9a34;
    --roof: #1f2530;
    --dusk: #e6b79a;
    --dune: #3b4a2c;
  }
  * { margin: 0; padding: 0; box-sizing: border-box; }
  html, body { width: 1166px; height: 1200px; overflow: hidden; }
  body { background: var(--canvas); position: relative; }

  .flyer-cover {
    position: absolute; left: 313px; top: 35px;
    width: 540px; height: 1130px;
    background: linear-gradient(180deg, var(--sky-top) 0%, var(--sky-bottom) 35%);
    overflow: hidden;
    box-shadow: 0 10px 30px rgba(0,0,0,.18);
  }
  .title-block { position: absolute; left: 0; top: 70px; width: 100%; text-align: center; color: var(--paper); }
  .title-rule { position: absolute; height: 1.5px; background: var(--paper); opacity: .9; }
  .title-rule--top { left: 80px; right: 50px; top: 0; }
  .title-rule--bottom { left: 50px; right: 30px; top: 128px; }
  .title-script {
    font-family: "Sacramento", cursive; font-size: 118px; line-height: 1;
    position: absolute; left: 0; right: 0; top: 8px;
  }
  .title-sub {
    position: absolute; left: 0; right: 0; top: 140px;
    font-family: "Questrial", sans-serif; font-size: 48px; letter-spacing: 1px;
  }
  .title-sub strong { font-family: "Montserrat", sans-serif; font-weight: 700; font-size: 64px; margin-left: 6px; }

  .photo-house {
    position: absolute; left: 0; top: 330px; width: 100%; height: 330px;
    background: linear-gradient(180deg, var(--sky-bottom) 0%, #a9cbe3 18%, var(--roof) 30%, #8d4b38 55%, var(--lawn) 75%, #4f8a2c 100%);
  }
  .photo-beach {
    position: absolute; left: 0; top: 800px; width: 100%; height: 330px;
    background: linear-gradient(180deg, #9eb4c4 0%, var(--dusk) 20%, #7d8f98 35%, #a89a86 55%, var(--dune) 80%, #26301d 100%);
  }

  .location-band { position: absolute; left: 0; top: 630px; width: 100%; height: 200px; }
  .location-band svg.band-shape { position: absolute; inset: 0; }
  .island-map {
    position: absolute; left: 40px; top: 40px; width: 60px; height: 130px;
    background: rgba(255,255,255,.85); border-radius: 6px;
  }
  .location-pin { position: absolute; left: 40px; top: -30px; width: 60px; height: 74px; }
  .location-text { position: absolute; left: 130px; top: 34px; color: var(--paper); }
  .location-lead { font-family: "Questrial", sans-serif; font-size: 30px; line-height: 1.15; }
  .location-name { font-family: "Sacramento", cursive; font-size: 92px; line-height: .95; margin-top: -2px; }
</style>
</head>
<body>
  <main class="flyer-cover">
    <header class="title-block">
      <span class="title-rule title-rule--top"></span>
      <h1 class="title-script">Ferienhaus</h1>
      <span class="title-rule title-rule--bottom"></span>
      <p class="title-sub">auf <strong>Sylt</strong></p>
    </header>

    <div class="photo-house" role="img" aria-label="Foto: rotes Backsteinhaus mit dunklem Reetdach, weißer Tür und großem Rasengrundstück unter blauem Himmel"></div>

    <div class="photo-beach" role="img" aria-label="Foto: Holzsteg durch die Dünen zum Meer bei Sonnenuntergang, mit weißem Anker-Symbol"></div>

    <section class="location-band">
      <svg class="band-shape" viewBox="0 0 540 200" preserveAspectRatio="none" aria-hidden="true">
        <polygon fill="#ffffff" points="0,22 30,16 60,24 95,12 130,20 170,10 210,18 250,8 290,16 330,6 370,14 410,4 450,12 490,2 540,8 540,176 500,182 460,174 420,186 380,178 340,190 300,182 260,194 220,186 180,196 140,188 100,198 60,190 20,198 0,192"/>
        <polygon fill="var(--band)" points="0,30 35,24 70,32 105,20 140,28 180,18 220,26 260,16 300,24 340,14 380,22 420,12 460,20 500,10 540,16 540,168 500,174 460,166 420,178 380,170 340,182 300,174 260,186 220,178 180,188 140,180 100,190 60,182 20,190 0,184"/>
      </svg>
      <div class="island-map" role="img" aria-label="Umrisskarte der Insel Sylt"></div>
      <svg class="location-pin" viewBox="0 0 60 74" aria-hidden="true">
        <path d="M30 70 C14 48 6 36 6 26 A24 24 0 0 1 54 26 C54 36 46 48 30 70Z" fill="none" stroke="#ffffff" stroke-width="5"/>
        <circle cx="30" cy="26" r="8" fill="#ffffff"/>
      </svg>
      <div class="location-text">
        <p class="location-lead">im ruhigen und<br>traditionellen Ort</p>
        <p class="location-name">Archsum</p>
      </div>
    </section>
  </main>
</body>
</html>
```